Brisk Harbor
Where Your Harbor Counts
Brisk Harbor - Consulting
Creative Brief
Professional
Marlo Fenwick
4817 Tulip Meadow Lane San Diego, CA 92143
briskharbor1@plumetide.com
I would like to have my logo on one side and see a monogram on the front, but all designs are welcome, thanks.

```html
<!DOCTYPE html>
<html lang="en">
<head>
<meta charset="utf-8">
<title>Brisk Harbor – Business Card</title>
<link rel="stylesheet" href="https://fonts.googleapis.com/css2?family=Open+Sans:wght@400;700&display=swap">
<style>
  :root {
    --backdrop: #b38d2f;
    --card-white: #ffffff;
    --brand-blue: #1f4f9c;
    --band-blue: #1b3f8f;
    --band-light: #3c6cc4;
    --back-center: #2a6fd0;
    --back-edge: #0a2466;
    --accent-orange: #f08a1c;
    --ink: #222222;
    --link-blue: #1f63c4;
  }
  html, body {
    margin: 0;
    padding: 0;
    width: 1200px;
    height: 686px;
    overflow: hidden;
    background: var(--backdrop);
    font-family: "Open Sans", Arial, sans-serif;
  }
  .canvas {
    position: relative;
    width: 1200px;
    height: 686px;
  }
  .card {
    position: absolute;
    width: 509px;
    height: 293px;
    border-radius: 26px;
    overflow: hidden;
    box-shadow: 0 4px 10px rgba(0,0,0,0.25);
  }
  .card-front {
    left: 67px;
    top: 132px;
    background: var(--card-white);
  }
  .card-back {
    left: 619px;
    top: 307px;
    background: radial-gradient(ellipse at 50% 45%, var(--back-center) 0%, #1c4fae 45%, var(--back-edge) 100%);
  }
  .corner-band {
    position: absolute;
    right: 0;
    top: 0;
    width: 260px;
    height: 80px;
  }
  .holder-name {
    position: absolute;
    right: 56px;
    top: 20px;
    margin: 0;
    color: #ffffff;
    font-size: 17px;
    font-weight: 700;
  }
  .brand-lockup {
    position: absolute;
    left: 0;
    right: 0;
    top: 118px;
    display: flex;
    justify-content: center;
    align-items: center;
    gap: 12px;
  }
  .brand-dot {
    width: 16px;
    height: 16px;
    border-radius: 50%;
    background: var(--accent-orange);
  }
  .brand-name {
    margin: 0;
    color: var(--brand-blue);
    font-size: 38px;
    font-weight: 700;
    letter-spacing: 1px;
    text-transform: uppercase;
  }
  .contact {
    position: absolute;
    left: 0;
    right: 0;
    top: 210px;
    text-align: center;
    font-size: 13.5px;
    color: var(--ink);
    line-height: 1.6;
  }
  .contact p { margin: 0; }
  .contact .label {
    color: var(--link-blue);
    font-weight: 700;
  }
  .back-lockup {
    position: absolute;
    inset: 0;
    display: flex;
    justify-content: center;
    align-items: center;
    gap: 14px;
  }
  .back-lockup .brand-name {
    color: var(--accent-orange);
    font-size: 40px;
  }
</style>
</head>
<body>
<main class="canvas">
  <section class="card card-front" aria-label="Card front">
    <svg class="corner-band" viewBox="0 0 260 80" aria-hidden="true">
      <defs>
        <linearGradient id="bandFill" x1="0" y1="0" x2="1" y2="1">
          <stop offset="0" stop-color="var(--band-light)"/>
          <stop offset="1" stop-color="var(--band-blue)"/>
        </linearGradient>
      </defs>
      <path d="M0 0 H260 V66 H120 Q80 66 60 40 Q40 10 0 0 Z" fill="url(#bandFill)"/>
    </svg>
    <p class="holder-name">Marlo Fenwick</p>
    <div class="brand-lockup">
      <span class="brand-dot"></span>
      <h1 class="brand-name">Brisk Harbor</h1>
    </div>
    <div class="contact">
      <p>4817 Tulip Meadow Lane San Diego, CA 92143</p>
      <p><span class="label">Email</span> : briskharbor1@plumetide.com</p>
    </div>
  </section>
  <section class="card card-back" aria-label="Card back">
    <div class="back-lockup">
      <span class="brand-dot"></span>
      <p class="brand-name">Brisk Harbor</p>
    </div>
  </section>
</main>
</body>
</html>
```